Australian Craft Distillery needs poster layout for its awesome Manifesto

Tall Finch's a small craft distillery based in the Brook Flats of Western Australia producing award-winning vodkas and gin. Check out our website www.tallfinchs-example.com.au to get a feel for our design aesthetic, especially from our bottle design. We are "Small Batch Liquors - Out of the Brook Flats". Everything we do reflects that.
We have a manifesto - The Tall Finch's Manifesto -that we proudly display in our tasting room, and was used as a basis for an artwork in our entry.
We've had a number of customers ask to buy a poster of the manifesto (attached) so I want to commission a more professional design than the current layout which was put together in Word! (yes I know, I'm sorry, I did move it into Illustrator later).
I think the text flows in a sequential order so I'm looking for a design that you read from start to finish rather than a random collection of statements. I'd like to include our logo in the design somewhere but it doesn't have to be front and centre. There is a secondary logo device as well - the interlocked T and F on the label which could be used. I'm assuming the print will be simple black on either a plain background or a "craft background" similar to the labels. Our current fonts are SchmutzICG for text and VeneerTwo for headings. The label uses Haymaker and Gin-Rough.
Print size will be A3 (prefer the design to be to this proportion and portrait orientation) and bigger up to A1. We'll print the final design on the back of t-shirts for staff as well. If I was going to sum up our style in a couple of words it would be "intelligently irreverent" Have fun with this, I certainly did writing it!

```html
<!DOCTYPE html>
<html lang="en">
<head>
<meta charset="utf-8">
<title>The Tall Finch's Manifesto</title>
<link rel="stylesheet" href="https://fonts.googleapis.com/css2?family=Bebas+Neue&family=Bitter:wght@700&family=Special+Elite&display=swap">
<style>
  :root {
    --paper: #deddcc;
    --ink: #2b2b2b;
    --ink-soft: #5a5a55;
    --cream: #efeed9;
    --heading: "Bebas Neue", "Arial Narrow", sans-serif;
    --body: "Bitter", Georgia, serif;
    --type: "Special Elite", "Courier New", monospace;
  }
  html, body { margin: 0; padding: 0; overflow: hidden; }
  body { width: 800px; height: 1200px; background: var(--paper); color: var(--ink); }
  .poster { position: relative; width: 800px; height: 1200px; overflow: hidden; }

  .ribbon { position: absolute; display: flex; align-items: center; justify-content: center; }
  .ribbon svg { position: absolute; inset: 0; width: 100%; height: 100%; }
  .ribbon-shape { fill: var(--cream); stroke: var(--ink); stroke-width: 2.5; vector-effect: non-scaling-stroke; }
  .ribbon-inner { fill: none; stroke: var(--ink-soft); stroke-width: 1.2; vector-effect: non-scaling-stroke; }
  .ribbon-label { position: relative; font-family: var(--heading); margin: 0; font-weight: 400; letter-spacing: 0.5px; line-height: 1; padding-top: 4px; }

  .title-ribbon { left: 130px; top: 84px; width: 570px; height: 84px; }
  .title-ribbon .ribbon-label { font-size: 50px; }

  .section-ribbon { height: 64px; }
  .section-ribbon .ribbon-label { font-size: 40px; }
  .first-ribbon { left: 305px; top: 196px; width: 175px; }
  .then-ribbon { left: 317px; top: 378px; width: 175px; }
  .finally-ribbon { left: 262px; top: 838px; width: 290px; }

  .mark { position: absolute; width: 34px; height: 34px; border-radius: 50%; background: var(--ink); box-shadow: 2px 3px 4px rgba(0,0,0,0.25); }
  .first-mark { left: 528px; top: 211px; }
  .then-mark { left: 540px; top: 393px; }
  .finally-mark { left: 592px; top: 853px; }

  .tenets { position: absolute; left: 0; width: 800px; margin: 0; padding: 0; list-style: none;
    text-align: center; font-family: var(--body); font-weight: 700; font-size: 15.5px; line-height: 21px; }
  .tenets li { white-space: nowrap; }
  .sep { display: inline-block; width: 7px; height: 7px; border-radius: 50%; background: var(--ink-soft); margin: 0 6px; vertical-align: 2px; }
  .first-list { top: 270px; }
  .then-list { top: 452px; }
  .finally-list { top: 918px; }

  .illustration { position: absolute; left: 96px; top: 648px; width: 228px; height: 190px;
    background: linear-gradient(135deg, #ecebd3 0%, #b9b8a8 55%, #6c6b66 100%); border-radius: 10px; }

  .brand { position: absolute; left: 350px; top: 695px; width: 370px; text-align: center; }
  .brand-name { font-family: var(--heading); font-size: 84px; line-height: 1; margin: 0; letter-spacing: 1px; color: var(--ink); }
  .brand-tagline { font-family: var(--type); font-size: 22px; margin: 4px 0 0; color: var(--ink); letter-spacing: 1px; }
</style>
</head>
<body>
<main class="poster">

  <header class="ribbon title-ribbon">
    <svg viewBox="0 0 200 60" preserveAspectRatio="none" aria-hidden="true">
      <polygon class="ribbon-shape" points="1,3 199,3 190,30 199,57 1,57 10,30"/>
      <polygon class="ribbon-inner" points="14,9 186,9 181,30 186,51 14,51 19,30"/>
    </svg>
    <h1 class="ribbon-label">The Tall Finch's Manifesto</h1>
  </header>

  <div class="ribbon section-ribbon first-ribbon">
    <svg viewBox="0 0 200 60" preserveAspectRatio="none" aria-hidden="true">
      <polygon class="ribbon-shape" points="1,3 199,3 186,30 199,57 1,57 14,30"/>
      <polygon class="ribbon-inner" points="20,9 180,9 172,30 180,51 20,51 28,30"/>
    </svg>
    <h2 class="ribbon-label">First…</h2>
  </div>
  <span class="mark first-mark"></span>
  <ul class="tenets first-list">
    <li>Work Smart<span class="sep"></span>Love Hard<span class="sep"></span>Play Often<span class="sep"></span>Sleep More</li>
    <li>Stay Present<span class="sep"></span>Be Local<span class="sep"></span>Embrace Silly<span class="sep"></span>Get Dirty (but) Stay Clean</li>
    <li>Laugh<span class="sep"></span>Cry<span class="sep"></span>Run<span class="sep"></span>Dance<span class="sep"></span>Sing</li>
    <li>Stop That (and) Slow down</li>
  </ul>

  <div class="ribbon section-ribbon then-ribbon">
    <svg viewBox="0 0 200 60" preserveAspectRatio="none" aria-hidden="true">
      <polygon class="ribbon-shape" points="1,3 199,3 186,30 199,57 1,57 14,30"/>
      <polygon class="ribbon-inner" points="20,9 180,9 172,30 180,51 20,51 28,30"/>
    </svg>
    <h2 class="ribbon-label">Then …</h2>
  </div>
  <span class="mark then-mark"></span>
  <ul class="tenets then-list">
    <li>Celebrate others success<span class="sep"></span>Don’t be shit</li>
    <li>Have one thing you are awesome at<span class="sep"></span>Get off your phone</li>
    <li>Show some fucking passion<span class="sep"></span>Make something</li>
    <li>Making money doesn’t count<span class="sep"></span>Making babies does</li>
    <li>Never stop exploring, never stop learning, share that with others</li>
    <li>We all fuck up</li>
    <li>Make good, learn, be better and move on</li>
    <li>Life is far too short, squeeze every drop out of it</li>
    <li>and, of course …</li>
    <li>Drink better</li>
  </ul>

  <div class="illustration" role="img" aria-label="Illustration of a bearded gentleman raising a frothy mug"></div>
  <div class="brand">
    <p class="brand-name">Tall Finch's</p>
    <p class="brand-tagline">Small Batch Liquors</p>
  </div>

  <div class="ribbon section-ribbon finally-ribbon">
    <svg viewBox="0 0 200 60" preserveAspectRatio="none" aria-hidden="true">
      <polygon class="ribbon-shape" points="1,3 199,3 190,30 199,57 1,57 10,30"/>
      <polygon class="ribbon-inner" points="14,9 186,9 180,30 186,51 14,51 20,30"/>
    </svg>
    <h2 class="ribbon-label">And Finally …</h2>
  </div>
  <span class="mark finally-mark"></span>
  <ul class="tenets finally-list">
    <li>Sometimes you just won’t understand<span class="sep"></span>An argument is not a fight</li>
    <li>You are not as important as you think<span class="sep"></span>You are more loved than you think</li>
    <li>Its ok to do things alone<span class="sep"></span>Its ok not to be busy</li>
    <li>There is no good reason to do a half arsed job</li>
    <li>Teaching is the best way of learning</li>
    <li>The past is important, what you do next is much more so</li>
    <li>Change is inevitable, roll with it</li>
    <li>Success is whatever you decide it to be</li>
  </ul>

</main>
</body>
</html>
```